1923 Basins & Spouts Business Card

I'm wanting to get a business card designed. Our business is 1923 Basins & Spouts
Details for the card:

1923 Basins & Spouts
Name: Gareth Vostle
Email: gareth@1923basinsandspouts.com.au
Website: www.1923basinsandspouts.com.au
Mobile: 0439 602 158
Phone: 02 5550 1843

Font of Basins & Spouts is called Snell Roundhand. Not sue what font logo text is.

I'm thinking two sided but it doesn't have to be.

```html
<!DOCTYPE html>
<html lang="en">
<head>
<meta charset="utf-8">
<title>1923 Basins &amp; Spouts – Business Card</title>
<link rel="stylesheet" href="https://fonts.googleapis.com/css2?family=Open+Sans:wght@400;600&family=Pinyon+Script&display=swap">
<style>
  :root {
    --backdrop: #343436;
    --card: #1d1e20;
    --card-pattern: #26272a;
    --ink: #ffffff;
    --ink-soft: #cfcfcf;
    --rule: #6a6a6c;
  }
  * { box-sizing: border-box; margin: 0; padding: 0; }
  html, body { width: 1200px; height: 1108px; overflow: hidden; }
  body {
    background: var(--backdrop);
    font-family: "Open Sans", Arial, sans-serif;
    position: relative;
  }
  .card {
    position: absolute;
    top: 209px;
    width: 420px;
    height: 690px;
    background: var(--card);
    border-radius: 22px;
    box-shadow: 0 12px 30px rgba(0,0,0,0.45);
    overflow: hidden;
  }
  .card--front { left: 150px; }
  .card--back { left: 630px; }

  .brand-mark {
    display: flex;
    align-items: center;
    justify-content: center;
    gap: 12px;
    color: var(--ink);
    font-family: "Open Sans", Arial, sans-serif;
    font-weight: 400;
  }
  .brand-mark__dot {
    width: 14px; height: 14px;
    border-radius: 50%;
    background: var(--ink);
  }
  .brand-mark__name { font-size: 40px; letter-spacing: 2px; line-height: 1; }

  .card--front .brand-mark { position: absolute; top: 118px; left: 0; right: 0; }
  .brand-title {
    position: absolute; top: 180px; left: 0; right: 0;
    text-align: center;
    font-family: "Pinyon Script", cursive;
    font-weight: 400;
    font-size: 52px;
    color: var(--ink);
    line-height: 1;
  }
  .tagline {
    position: absolute; top: 252px; left: 0; right: 0;
    text-align: center;
    font-size: 12.5px;
    color: var(--ink-soft);
  }
  .person-name {
    position: absolute; top: 400px; left: 0; right: 0;
    text-align: center;
    font-family: "Pinyon Script", cursive;
    font-weight: 400;
    font-size: 40px;
    color: var(--ink);
    line-height: 1;
  }
  .name-rule {
    position: absolute; top: 458px; left: 95px; right: 95px;
    border-top: 1px solid var(--rule);
  }
  .contact {
    position: absolute; top: 476px; left: 0; right: 0;
    text-align: center;
    list-style: none;
    font-size: 17px;
    line-height: 25px;
    color: var(--ink-soft);
  }
  .contact__label { font-weight: 600; color: var(--ink); }

  .pattern-field {
    position: absolute; inset: 0;
    background: radial-gradient(circle at 50% 50%, var(--card-pattern), var(--card) 75%);
  }
  .card--back .brand-mark {
    position: absolute; top: 50%; left: 0; right: 0;
    transform: translateY(-50%);
  }
  .card--back .brand-mark__name { font-size: 34px; }
</style>
</head>
<body>
  <section class="card card--front" aria-label="Business card front">
    <div class="brand-mark">
      <span class="brand-mark__dot"></span>
      <span class="brand-mark__name">1923</span>
    </div>
    <h1 class="brand-title">Basins &amp; Spouts</h1>
    <p class="tagline">Pairing classic elegance with everyday dependability</p>
    <h2 class="person-name">Gareth Vostle</h2>
    <div class="name-rule"></div>
    <ul class="contact">
      <li><span class="contact__label">P:</span> 0439 602 158</li>
      <li><span class="contact__label">M:</span> 02 5550 1843</li>
      <li>gareth@1923basinsandspouts.com.au</li>
      <li>www.1923basinsandspouts.com.au</li>
    </ul>
  </section>

  <section class="card card--back" aria-label="Business card back">
    <div class="pattern-field" role="img" aria-label="Faint repeating brand pattern across the card back"></div>
    <div class="brand-mark">
      <span class="brand-mark__dot"></span>
      <span class="brand-mark__name">1923</span>
    </div>
  </section>
</body>
</html>
```